IT Services Postcard

I am looking to update and refresh my existing postcard. I would like to keep all the content it has , but make it more modern and elegant. We are a small boutique IT firm here in Miami, FL in business for 15 years. We support all Veltrosa products. I would like highlight that as well on the postcard- "15 years serving South Florida". I would also like to make the following revisions to the bullet points:Change "Included Email & Virus Protection" to Included Antivirus SoftwareChange "Quarnex Plus Remote Control" to "Secure remote computer access"Add the following bullet point "Included Deskora 520 Backup"You can certainly change the images for the bullet points, and refresh the colors and background as well. I have uploaded a copy of the front and back of my last flyer. I target small to medium size businesses who need a good local IT company they can trust. I look forward to working with you. Thank you.
Target Market(s)
Small Businesses
Industry/Entity Type
It Professional
Colors
Designer to choose colors to be used in the design.
Look and feel

```html
<!DOCTYPE html>
<html lang="en">
<head>
<meta charset="utf-8">
<title>Corvan Tech Postcard</title>
<link rel="stylesheet" href="https://fonts.googleapis.com/css2?family=Open+Sans:wght@400;600;700;800&display=swap">
<style>
  :root{
    --bg:#e4e4e2;
    --paper:#ffffff;
    --ink:#1d1d1f;
    --blue:#1f7cc4;
    --orange:#e56f12;
    --band:#1c1c1c;
    --muted:#4a4f55;
    --photo-a:#6b5446;
    --photo-b:#c9b9a6;
    --photo-c:#3a3f44;
    --photo-d:#a89a85;
  }
  *{box-sizing:border-box;margin:0;padding:0}
  html,body{width:1200px;height:900px;overflow:hidden}
  body{background:var(--bg);font-family:"Open Sans",Arial,sans-serif;color:var(--ink);position:relative}
  .card{position:absolute;top:250px;width:560px;height:390px;background:var(--paper);overflow:hidden;box-shadow:0 6px 18px rgba(0,0,0,.18)}
  .card--front{left:25px}
  .card--back{left:615px}
  .stripes{position:absolute;left:0;top:0;pointer-events:none}

  /* brand */
  .brand{position:absolute;display:inline-block}
  .brand__name{font-weight:800;color:var(--ink);line-height:1;letter-spacing:1px}
  .brand__tag{font-weight:700;color:var(--ink);text-align:right;letter-spacing:1.5px}
  .brand--large{left:22px;top:26px}
  .brand--large .brand__name{font-size:30px}
  .brand--large .brand__tag{font-size:10px}
  .brand--small{left:405px;top:108px}
  .brand--small .brand__name{font-size:14px}
  .brand--small .brand__tag{font-size:5.5px;letter-spacing:1px}

  /* front */
  .front-photo{position:absolute;left:0;top:0;width:560px;height:345px;
    background:linear-gradient(160deg,var(--photo-a),var(--photo-b) 70%,#eee);
    clip-path:polygon(360px 0,560px 0,560px 345px,430px 345px,390px 160px)}
  .headline{position:absolute;left:22px;top:86px;width:320px}
  .headline__ask{color:var(--blue);font-weight:800;font-size:12px;text-transform:uppercase;white-space:nowrap}
  .headline__answer{font-weight:700;font-size:17px;text-transform:uppercase;line-height:1.25}
  .tab{position:absolute;left:22px;background:var(--blue);color:#fff;font-weight:700;font-size:11px;line-height:1;padding:5px 12px 5px 8px;text-transform:uppercase}
  .tab--services{top:134px}
  .tab--other{top:274px}
  .list{position:absolute;list-style:none;font-size:9.5px;line-height:12px;color:var(--muted)}
  .list li{padding-left:11px;position:relative;margin-bottom:2px}
  .list li::before{content:"\2713";position:absolute;left:0;color:var(--blue);font-weight:700}
  .list--left{left:22px;top:160px;width:155px}
  .list--right{left:185px;top:138px;width:140px;border-left:1px solid var(--blue);padding-left:10px}
  .list--other{left:22px;top:298px;width:225px}
  .badges{position:absolute;left:252px;top:304px;display:flex;gap:8px}
  .badge{width:30px;height:18px;border-radius:2px;background:#dfe7ef;border:1px solid #b8c6d4}
  .badge--blue{background:var(--blue);border-color:var(--blue)}
  .front-band{position:absolute;left:0;bottom:0;width:100%;height:45px;background:var(--band);color:#fff;font-size:12px;display:flex;align-items:center;justify-content:space-between;padding:0 22px}
  .contact{display:flex;align-items:center;gap:6px}

  /* back */
  .back-photo{position:absolute;left:0;top:0;width:390px;height:390px;
    background:linear-gradient(150deg,var(--photo-c),var(--photo-d) 55%,var(--photo-c));
    clip-path:polygon(0 0,345px 0,385px 170px,360px 390px,0 390px)}
  .back-headline{position:absolute;left:0;top:70px;width:350px;background:rgba(20,20,20,.78);padding:8px 14px;color:#fff}
  .back-headline__lead{color:var(--orange);font-weight:800;font-size:12px;text-transform:uppercase}
  .back-headline__years{font-weight:800;font-size:13.5px;text-transform:uppercase}
  .back-headline__serve{font-weight:400;font-size:14px;text-transform:uppercase;color:#ddd}
  .phone{position:absolute;left:240px;top:312px;width:125px;background:var(--blue);color:#fff;font-size:13px;padding:3px 8px;display:flex;align-items:center;gap:5px}
  .back-band{position:absolute;left:0;bottom:0;width:345px;height:38px;background:var(--blue);color:#fff;font-size:13px;display:flex;align-items:center;gap:6px;padding-left:16px}
  .stamp{position:absolute;right:22px;top:20px;width:70px;height:70px;border:1.5px solid #333}
  .address-line{position:absolute;left:410px;width:130px;border-top:1.5px solid #333}
  .address-line--1{top:175px}
  .address-line--2{top:205px}
  .address-line--3{top:235px}
</style>
</head>
<body>

<section class="card card--front">
  <div class="front-photo" role="img" aria-label="Photo of a smiling woman working on a laptop in an office"></div>
  <svg class="stripes" width="560" height="390" viewBox="0 0 560 390" aria-hidden="true">
    <polyline points="325,0 355,160 395,345" fill="none" stroke="var(--orange)" stroke-width="7"/>
    <polyline points="338,0 368,160 408,345" fill="none" stroke="var(--blue)" stroke-width="4"/>
  </svg>

  <div class="brand brand--large">
    <div class="brand__name">CORVAN TECH</div>
    <div class="brand__tag">MANAGED SERVICES</div>
  </div>

  <div class="headline">
    <div class="headline__ask">Are computer problems frustrating you?</div>
    <div class="headline__answer">We can help!</div>
  </div>

  <div class="tab tab--services">Our IT Service :</div>
  <ul class="list list--left">
    <li>24/7 monitoring of servers</li>
    <li>proactive desktop &amp; server maintenance</li>
    <li>fast response times</li>
    <li>Included Deskora 520 Backup</li>
    <li>Included Antivirus Software Change</li>
  </ul>
  <ul class="list list--right">
    <li>Secure remote computer access</li>
    <li>unlimited onsite &amp; Remote support</li>
    <li>monthly network health report</li>
    <li>Veltrosa certified technicians</li>
    <li>no long term contracts</li>
  </ul>

  <div class="tab tab--other">Other services offered:</div>
  <ul class="list list--other">
    <li>Brivana business voice edge installation</li>
    <li>onsite/offsite backup solutions</li>
  </ul>

  <div class="badges" aria-label="Partner badges">
    <span class="badge"></span><span class="badge badge--blue"></span><span class="badge"></span>
  </div>

  <div class="front-band">
    <span class="contact">
      <svg width="11" height="11" viewBox="0 0 11 11" aria-hidden="true"><circle cx="5.5" cy="5.5" r="5" fill="none" stroke="#fff"/><ellipse cx="5.5" cy="5.5" rx="2.2" ry="5" fill="none" stroke="#fff"/><line x1="0.5" y1="5.5" x2="10.5" y2="5.5" stroke="#fff"/></svg>
      www.corvantech.com
    </span>
    <span class="contact">
      <svg width="12" height="9" viewBox="0 0 12 9" aria-hidden="true"><rect x="0.5" y="0.5" width="11" height="8" fill="none" stroke="#fff"/><polyline points="0.5,0.5 6,5 11.5,0.5" fill="none" stroke="#fff"/></svg>
      support@corvantech.com
    </span>
  </div>
</section>

<section class="card card--back">
  <div class="back-photo" role="img" aria-label="Photo of hands typing on a laptop while holding a smartphone"></div>
  <svg class="stripes" width="560" height="390" viewBox="0 0 560 390" aria-hidden="true">
    <polyline points="350,0 390,170 365,390" fill="none" stroke="var(--orange)" stroke-width="6"/>
    <polyline points="362,0 402,170 377,390" fill="none" stroke="var(--blue)" stroke-width="4"/>
  </svg>

  <div class="back-headline">
    <div class="back-headline__lead">We are a small boutique IT firm here in Miami</div>
    <div class="back-headline__years">FL in business for 15 years.</div>
    <div class="back-headline__serve">15 years serving South Florida</div>
  </div>

  <div class="phone">
    <svg width="10" height="10" viewBox="0 0 10 10" aria-hidden="true"><path d="M2 0.5 L3.6 2.8 L2.6 3.9 Q3.8 6.3 6.1 7.4 L7.2 6.4 L9.5 8 L8.4 9.5 Q3.6 9 0.5 1.6 Z" fill="#fff"/></svg>
    305 555 0148
  </div>
  <div class="back-band">
    <svg width="11" height="11" viewBox="0 0 11 11" aria-hidden="true"><circle cx="5.5" cy="5.5" r="5" fill="none" stroke="#fff"/><ellipse cx="5.5" cy="5.5" rx="2.2" ry="5" fill="none" stroke="#fff"/><line x1="0.5" y1="5.5" x2="10.5" y2="5.5" stroke="#fff"/></svg>
    www.corvantech.com
  </div>

  <div class="brand brand--small">
    <div class="brand__name">CORVAN TECH</div>
    <div class="brand__tag">MANAGED SERVICES</div>
  </div>
  <div class="stamp" aria-label="Stamp area"></div>
  <div class="address-line address-line--1"></div>
  <div class="address-line address-line--2"></div>
  <div class="address-line address-line--3"></div>
</section>

</body>
</html>
```